residential/commercial designer. looking to expand customer base.

we need a postcard design for an established residential/commercial interior design firm. TRV Interiors has over 25 yrs experience in creating unique and timeless residential and commercial spaces. offering assistance with cabinet design & furniture, accessories, lighting, plumbing & finish selections in new construction and renovation projects. TRV Interiors has completed projects in New York, California, Florida and Arizona. we will work with clients builder and them to create their personal space. this allows project to progress smoothly and cost effectively.
want postcard simple, straight forward architectural design concept. not whimsical. maybe wanting to incorporate a tag line.
don't expect to include all photos on postcard. looking to your expert opinion on which words and photos should be included on postcard. i know i don't need to say "i want a design that people don't throw away when they receive it"
include: TRV Interiors, Unified Spaces, info@trvinteriorsdemo.com, 555-314-9082 , Maren Dovetti, Principal
please contact me with your questions
Target Market(s)
high end residential, high style commercial
Industry/Entity Type
Residential
Requirements
Must have
- TRV Interior
- Unified Spaces
- info@trvinteriorsdemo.com
- 555-314-9082
- Maren Dovetti, Principal
- best photos with most visual impact.
- use different photos to show design diversity and style
Nice to have
- tag line

```html
<!DOCTYPE html>
<html lang="en">
<head>
<meta charset="utf-8">
<title>TRV Interiors Postcard</title>
<link rel="stylesheet" href="https://fonts.googleapis.com/css2?family=Crimson+Text&family=Share+Tech+Mono&display=swap">
<style>
  :root {
    --gold: #e0b23a;
    --blue: #2f6fd8;
    --tan: #c3b07c;
    --olive: #5d6340;
    --mauve: #a59ba9;
    --brown: #3a2a1f;
    --white: #ffffff;
    --sand-text: #dcc590;
  }
  * { margin: 0; padding: 0; box-sizing: border-box; }
  html, body { width: 1200px; height: 807px; overflow: hidden; background: var(--brown); }
  .postcard { position: relative; width: 1200px; height: 807px; }

  .swatch-strip { position: absolute; top: 0; left: 0; width: 1200px; height: 27px; display: flex; }
  .swatch-strip div { flex: 1; }

  .info-band { position: absolute; top: 27px; left: 0; width: 1200px; height: 437px; background: var(--brown); }

  .brand { position: absolute; left: 130px; top: 66px; width: 394px; text-align: center; color: var(--white);
           font-family: "Crimson Text", serif; }
  .brand-name { font-size: 104px; line-height: 1; font-weight: 400; }
  .brand-name span { display: block; }
  .brand-name .sub { font-size: 94px; margin-top: 6px; }
  .brand-tag { font-size: 44px; margin-top: 18px; }

  .divider { position: absolute; left: 524px; top: 77px; width: 9px; height: 260px; background: var(--blue); }

  .contact { position: absolute; left: 562px; top: 70px; color: var(--sand-text);
             font-family: "Share Tech Mono", monospace; font-size: 38px; letter-spacing: 4px; line-height: 42px; list-style: none; }

  .tile-grid { position: absolute; top: 464px; left: 0; width: 1200px; height: 343px;
               display: grid; grid-template-columns: repeat(5, 240px); grid-template-rows: repeat(2, 171.5px); }
  .photo-dark { background: linear-gradient(160deg, #6b5a4a 0%, #2a221c 55%, #14100d 100%); }
  .photo-white { background: linear-gradient(150deg, #d9d3c8 0%, #8a7c6c 50%, #2b231d 100%); }
  .photo-night { background: linear-gradient(170deg, #3d4a55 0%, #1a1a1c 60%, #0c0b0b 100%); }
  .photo-warm { background: linear-gradient(160deg, #8b6b4a 0%, #3c2c20 60%, #1c140e 100%); }
  .photo-bar { background: linear-gradient(180deg, #2a211b 0%, #7a5a30 55%, #3a2a1c 100%); }
</style>
</head>
<body>
<div class="postcard">
  <div class="swatch-strip">
    <div style="background:var(--gold)"></div>
    <div style="background:var(--blue)"></div>
    <div style="background:var(--tan)"></div>
    <div style="background:var(--olive)"></div>
    <div style="background:var(--mauve)"></div>
  </div>

  <section class="info-band">
    <div class="brand">
      <h1 class="brand-name"><span>TRV</span><span class="sub">Interiors</span></h1>
      <p class="brand-tag">Unified Spaces</p>
    </div>
    <div class="divider"></div>
    <ul class="contact">
      <li>Unified Spaces</li>
      <li>info@trvinteriorsdemo.com</li>
      <li>555-314-9082</li>
      <li>Maren Dovetti, Principal</li>
    </ul>
  </section>

  <div class="tile-grid">
    <div class="photo-dark" role="img" aria-label="Photo of a dark kitchen with vaulted ceiling and island"></div>
    <div style="background:var(--blue)"></div>
    <div class="photo-white" role="img" aria-label="Photo of a bright white kitchen with island and stools"></div>
    <div style="background:var(--olive)"></div>
    <div class="photo-night" role="img" aria-label="Photo of a modern living room with large windows"></div>
    <div style="background:var(--gold)"></div>
    <div class="photo-warm" role="img" aria-label="Photo of a warm wood kitchen with dining table"></div>
    <div style="background:var(--tan)"></div>
    <div class="photo-bar" role="img" aria-label="Photo of a commercial bar with lit counter and stools"></div>
    <div style="background:var(--mauve)"></div>
  </div>
</div>
</body>
</html>
```